30 Yr Pizzeria needs the freshest and flyest new flyer menu designed

Hiya,

Bellu's Pizza has been making beautiful love filled pizzas for close to 30 years...and we're stepping it up.

Fresh menu, Fresh messaging, we're finally making a splash with social media, and we want to tell the world to try us out

This project is to create a Landscape A4 3 x panel menu to showcase our amazing pizzas and pastas (with the super tasty side orders.

Some pointers to get going:
- This the the link to all resources for this project (logos/descriptions/prices/pics etc), it's vew only
https://files.sharebinexample.com/folders/7kQwZp2Rt84LmNvXe5aBcDfGhJsYtU3oP?usp=sharing
- This is the 5 min video link of instructions and intro from me. If you want to nail this and win the contest, and design our super dooper menu, you need to watch this.
https://www.clipvistaexample.com/share/4a7c93e1f05b62d8c4e7a19b3f6d0e25
- For more images, check out our instagram #bellupizzamarshvale
- I am keen for a quick turn around time, so we can have it ready for printing before end of November.

Any questions or issue of access, please reach out to me.

Rgds
Osric

Target Market(s)

Families, Singles, hungry people, couples, more hungry people

Industry/Entity Type

Italian Restaurant

Font styles to use
Serif
Sans Serif

Colors
f48d91
ec1f27
f04a50
f59195
fbd4d5
0355a3
3176b5
85abd2
85acd3

Requirements
Must have
• Must - watch the vid - I explain what I want:
• https://www.clipvistaexample.com/share/4a7c93e1f05b62d8c4e7a19b3f6d0e25
• And view the 3rd tab on the Google Spreadsheet called:
• https://sheets.tablenookexample.com/spreadsheets/d/9Xte-QmR4WpL7Bz2Vn6cYkHsJdAfGuEoTyPiUqZrS3N/edit#gid=8273619054
• All the resources are in this folder:
• https://files.sharebinexample.com/drive/u/0/folders/7kQwZp2Rt84LmNvXe5aBcDfGhJsYtU3oP?ogsrc=32
Nice to have
• Make it efficient, easy on the eye, easy to read, and choose photos that stand out and make you hungry.
• Yes I Described a lot of detail - but please, it's a general guide, if you have little additions/suggestions
Should not have
• The colour green - of any shade. Nice reds/blues/blacks/greys etc....check out our instagram and facebook if you want to get idea of personality and style.
• No hard to read cursive texts

```html
<!DOCTYPE html>
<html lang="en">
<head>
<meta charset="utf-8">
<title>Bellu's Pizza – Menu</title>
<link href="https://fonts.googleapis.com/css2?family=Bebas+Neue&family=Oswald:wght@300;400&family=Signika:wght@500;600&family=Patrick+Hand&family=Montserrat:wght@600;700&family=Playfair+Display:ital@1&display=swap" rel="stylesheet">
<style>
:root{
  --red:#ec1f27;
  --red-deep:#d8262c;
  --red-soft:#f04a50;
  --pink:#f59195;
  --pink-pale:#f6c9cc;
  --pink-band:#f0a9ae;
  --blue:#3176b5;
  --blue-pale:#c9d9ec;
  --ink:#1d1d1d;
  --grey:#444;
  --paper:#fbfbfb;
  --veg:#3c8a2e;
  --kid:#e5b500;
}
*{margin:0;padding:0;box-sizing:border-box}
html,body{width:1200px;height:848px;overflow:hidden}
body{position:relative;background:var(--red-deep);font-family:"Patrick Hand",sans-serif;color:var(--ink)}

/* ---------- left story panel ---------- */
.story{position:absolute;left:0;top:0;width:432px;height:848px;overflow:hidden}
.story__wood{position:absolute;inset:0 0 360px 0;background:linear-gradient(100deg,#d9d6d2,#f1efec 40%,#e3e0dc 70%,#cfcbc6)}
.story__photo{position:absolute;left:0;right:0;top:470px;bottom:0;background:radial-gradient(ellipse at 45% 40%,#e9b44c 0%,#d0702c 40%,#8a2b17 75%,#3a1a10 100%)}
.story__title{position:absolute;left:42px;top:18px;color:var(--red);white-space:nowrap;line-height:52px}
.story__title b{font-family:"Bebas Neue",sans-serif;font-weight:400;font-size:54px;letter-spacing:1px}
.story__title span{font-family:"Oswald",sans-serif;font-weight:300;font-size:44px}
.story__body{position:absolute;left:42px;top:80px;width:372px;font-size:15.2px;line-height:16px;color:#222}
.story__body h3{font-family:"Oswald",sans-serif;font-weight:300;color:var(--red);font-size:18px;line-height:20px;margin-top:10px;text-transform:uppercase}
.guarantee{margin-top:10px}
.guarantee h4{font-family:"Oswald",sans-serif;font-weight:300;font-size:14px;border-bottom:2px dotted var(--red);display:inline-block;width:100%}
.guarantee p{font-family:"Montserrat",sans-serif;font-size:8.8px;line-height:16px;font-weight:600;font-variant:small-caps;letter-spacing:.3px}
.guarantee em{font-family:"Playfair Display",serif;font-size:13px;font-weight:400;font-variant:normal}
.markers{position:absolute;left:28px;top:426px;width:400px;height:50px;background:rgba(133,171,210,.55);border-top:2px dotted var(--red);padding:4px 14px;font-size:12.5px;color:#333}
.markers h4{position:absolute;left:172px;top:-6px;font-family:"Signika",sans-serif;font-weight:600;font-size:14px;color:#222;background:rgba(230,236,244,.9);padding:0 4px}
.markers ul{list-style:none;display:grid;grid-template-columns:150px 110px 120px;row-gap:2px;margin-top:12px}
.allergy{position:absolute;left:0;width:432px;top:804px;text-align:center;color:#fff;font-family:"Signika",sans-serif;font-weight:500;font-size:13.5px;line-height:14px}

/* ---------- markers ---------- */
.mk{display:inline-block;width:12px;height:12px;border-radius:50%;color:#fff;font-family:"Signika",sans-serif;font-weight:600;font-size:6.5px;line-height:12px;text-align:center;vertical-align:1px;margin-right:2px;border:1px solid #fff}
.mk--gf{background:var(--blue)}
.mk--cf{background:#e8336a}
.mk--v{background:var(--veg)}
.mk--kf{background:var(--kid)}
.mk--sf{background:var(--red)}

/* ---------- menu card ---------- */
.menu{position:absolute;left:452px;top:16px;width:732px;height:824px;background:var(--paper);border-top-right-radius:22px}
.menu__note{position:absolute;left:0;right:0;top:3px;text-align:center;font-family:"Montserrat",sans-serif;font-weight:700;font-size:8.4px;font-variant:small-caps;letter-spacing:.5px}
.block-head{font-family:"Bebas Neue",sans-serif;color:var(--red);font-size:33px;line-height:30px;letter-spacing:.5px}
.prices{display:grid;grid-template-columns:1fr 120px;font-family:"Montserrat",sans-serif;font-weight:700;font-size:10.3px;line-height:12.5px;font-variant:small-caps;letter-spacing:.4px}
.prices .xt{margin-top:-11px}
.price-extra{font-family:"Signika",sans-serif;font-weight:500;font-size:12.6px;line-height:13px}
.traditional{position:absolute;left:6px;top:14px;width:354px;height:538px;background:var(--pink-pale)}
.traditional__top{padding:4px 8px 0}
.vegan{background:var(--blue-pale);margin:8px 0 0;padding:4px 8px;font-family:"Signika",sans-serif;font-weight:500;font-size:11.5px;line-height:12.6px;height:48px}
.vegan small{font-family:"Montserrat",sans-serif;font-weight:700;font-size:9px;font-variant:small-caps}
.items{list-style:none;padding:0 8px}
.item{font-size:12.8px;line-height:13.4px;color:var(--grey)}
.item b{font-family:"Signika",sans-serif;font-weight:600;font-size:15px;color:var(--ink);margin-right:3px}
.traditional .items{margin-top:10px}
.traditional .item{margin-bottom:0}
.item--hl{background:var(--pink-band);margin:0 -8px;padding:0 8px}
.photo-slice{position:absolute;left:4px;top:540px;width:354px;height:146px;background:linear-gradient(160deg,#d9b24e,#f0cf78 40%,#c88a34 75%,#8b5a24)}
.gourmet{position:absolute;left:372px;top:14px;width:350px}
.gourmet .item{font-size:12.6px;line-height:13.2px}
.sec-head{font-family:"Oswald",sans-serif;font-weight:300;color:var(--red);font-size:21px;line-height:24px;display:flex;align-items:flex-end;gap:6px;margin-top:4px}
.sec-head::after{content:"";flex:1;border-bottom:3px dotted var(--red);margin-bottom:6px}
.gourmet .items{padding:0 0 0 2px}
.gourmet .item--hl{margin:0 -4px 0 -2px;padding:0 4px 0 2px}
.vegetarian{position:absolute;left:12px;top:700px;width:710px}
.vegetarian .items{padding:0}
.vegetarian .item{line-height:13.6px;font-size:12.6px}
</style>
</head>
<body>

<section class="story">
  <div class="story__wood" role="img" aria-label="Whitewashed timber boards background"></div>
  <div class="story__photo" role="img" aria-label="Close-up photo of a baked pizza with olives, pepperoni and melted cheese"></div>

  <h1 class="story__title"><b>A PIZZA</b> <span>LOVE STORY</span></h1>

  <div class="story__body">
    <p>Every morning, I begin making the dough for our famous crust. I use specially filtered water, and after all the ingredients are added (can't tell you what they are...it's a family secret) - I mix it for exactly 14 minutes.<br>After mixing, it goes into the proofing stage that can go up to 8 and a half hours (depending on the weather temperature). When it's right - I form individual dough balls - one of them will be for your pizza!</p>
    <h3>Is all this work a pain in the butt?</h3>
    <p>Yeah. But, our customers absolutely rave about our crust, so, I don't want to let them down.</p>
    <h3>Is it the best crust and pizza in town?</h3>
    <p>I think it is. But I know this for sure - it tastes better than that frozen "chain" store" crust with the cardboard taste that leaves you bloated hours after your last slice!</p>
    <div class="guarantee">
      <h4>OUR GUARANTEE</h4>
      <p>We put our soul into our pizzas. If for some reason your order didn't meet your expectations, let us know why. I'll refund your money and be grateful to you for trying us out. – <em>Master Pizzaiolo Bruno</em></p>
    </div>
  </div>

  <div class="markers">
    <h4>Markers</h4>
    <ul>
      <li><span class="mk mk--gf">GF</span> -Gluten Free Toppings</li>
      <li><span class="mk mk--v">V</span> -Fully Vegan</li>
      <li><span class="mk mk--sf">SF</span> - Staff Favourite</li>
      <li><span class="mk mk--cf">CF</span> - Cust Favourite</li>
      <li><span class="mk mk--kf">KF</span> - Loved by Kids</li>
    </ul>
  </div>

  <p class="allergy">Please tell us if you have any allergies<br>we should be aware of.</p>
</section>

<main class="menu">
  <p class="menu__note">All pizzas come with mozzarella cheese and a tomato sauce base (unless we specify differently)</p>

  <section class="traditional">
    <div class="traditional__top">
      <h2 class="block-head">Traditional Pizzas</h2>
      <div class="prices">
        <div>
          <p>Small - 23cm 9" - 11.96</p>
          <p>Medium - 28cm 11" - 15.95</p>
          <p>Large - 33cm 13" - 21.95</p>
          <p>Family - 38cm 15" - 24 95</p>
        </div>
        <div class="xt">
          <p>Extra Toppings</p>
          <p>1.00</p><p>1.00</p><p>2.00</p><p>2.00</p>
        </div>
      </div>
      <p class="price-extra">Half/Half Pizza Large &amp; Family Only,<br>Gluten Free Bases (Medium Only) add 4.95</p>
    </div>
    <p class="vegan">Can't have cheese? We use 'Kind Harvest' vegan cheese - <small>add 1.95 to small/medium, and 2.95 to large/ family</small></p>
    <ul class="items">
      <li class="item"><b>Margarita</b><span class="mk mk--v">V</span><span class="mk mk--cf">CF</span><span class="mk mk--kf">KF</span><span class="mk mk--gf">GF</span> Melting mozzarella cheese on a tomato base (ask for a pinch of oregano and basil).</li>
      <li class="item"><b>Meat Lovers</b><span class="mk mk--gf">GF</span> All the meat. Charred and juicy ham, cabanossi, pepperoni and beef with a shake of tangy BBQ sauce.</li>
      <li class="item"><b>Vegetarian</b><span class="mk mk--v">V</span><span class="mk mk--gf">GF</span> Freshly chopped capsicum, onion, mushrooms and pineapple.</li>
      <li class="item"><b>Supreme</b><span class="mk mk--gf">GF</span><span class="mk mk--cf">CF</span> Ham, mushroom, onion, cabanossi, capsicum and pineapple (ask for anchovies and olives for salty goodness).</li>
      <li class="item"><b>Mexicana</b><span class="mk mk--gf">GF</span> Spicy pepperoni and fresh cut capsicum (ask for a sprinkle of chilli for extra spicy)</li>
      <li class="item"><b>Australian</b><span class="mk mk--gf">GF</span> Ham and bacon with a fresh egg cracked over the top. Aussie as.</li>
      <li class="item"><b>Hawaiian</b><span class="mk mk--gf">GF</span><span class="mk mk--kf">KF</span> Thick cut ham and sweet tinned pineapple. Aloha!</li>
      <li class="item"><b>Napoli</b><span class="mk mk--gf">GF</span> Fresh and melting mozzarella with kalamata olives and anchovies.</li>
      <li class="item"><b>Ham and Cheese</b><span class="mk mk--gf">GF</span><span class="mk mk--kf">KF</span> Just cheese, just ham, just sauce. Plainly perfect.</li>
      <li class="item"><b>Pep'n'Mush</b><span class="mk mk--gf">GF</span> A piping hot pile of pepperoni and fresh mushrooms.</li>
      <li class="item"><b>Pepperoni</b><span class="mk mk--gf">GF</span><span class="mk mk--kf">KF</span> The Classic, New York Style. You want pepperoni? You got it.</li>
      <li class="item"><b>Bellu's Capricciosa</b><span class="mk mk--gf">GF</span> Bellu's take: ham, fresh mushrooms and kalamata olives (ask for anchovies)</li>
      <li class="item"><b>Funghi</b><span class="mk mk--gf">GF</span><span class="mk mk--v">V</span> Miles of mushrooms with a touch of shallots.</li>
    </ul>
  </section>

  <div class="photo-slice" role="img" aria-label="Photo of a cheesy pizza slice topped with a basil leaf"></div>

  <section class="gourmet">
    <h2 class="block-head">Goumet Pizzas</h2>
    <div class="prices">
      <div>
        <p>Small - 23cm 9" - 12.96</p>
        <p>Medium - 28cm 11" - 16.95</p>
        <p>Large - 33cm 13" - 22.95</p>
        <p>Family - 38cm 15" - 25 95</p>
      </div>
      <div class="xt">
        <p>Extra Toppings</p>
        <p>1.00</p><p>1.00</p><p>2.00</p><p>2.00</p>
      </div>
    </div>
    <p class="price-extra">Half/Half Pizza Large &amp; Family Only,<br>Gluten Free Bases (Medium Only) add 4.95</p>

    <h3 class="sec-head">SEAFOOD GOURMET</h3>
    <ul class="items">
      <li class="item"><b>Bellu's Four Seasons</b><span class="mk mk--gf">GF</span> Prawns, fresh cut capsicum, pineapple and mushrooms with tangy BBQ sauce.</li>
      <li class="item"><b>Marshvale Special</b><span class="mk mk--gf">GF</span> Fresh chunks of juicy tuna with onion, pineapple, capsicum and mushrooms.</li>
      <li class="item item--hl"><b>Bellu's Special Supreme</b><span class="mk mk--cf">CF</span><span class="mk mk--gf">GF</span> Supreme plus added garlic prawns (ask for the Salty Special Supreme for anchovies and olives)</li>
      <li class="item"><b>Marinara</b><span class="mk mk--gf">GF</span> Prawns, mussels, and baby octopus, sprinkled with fresh chopped garlic and basil.</li>
      <li class="item"><b>Al Caprawn</b><span class="mk mk--gf">GF</span> Prawns, roasted capsicum, pineapple and onion on sweet chilli sauce, all topped with a blob of of sour cream.</li>
    </ul>

    <h3 class="sec-head">MEAT GOURMET</h3>
    <ul class="items">
      <li class="item"><b>Pointing Special</b><span class="mk mk--gf">GF</span> Seasoned beef, fresh sliced mushrooms and onions.</li>
      <li class="item"><b>Spicy Night Breakfast</b><span class="mk mk--gf">GF</span> Spicy and aromatic Sujuk sausage, a fresh cracked egg and chunky cut fresh tomatoes. Start the night - right.</li>
      <li class="item item--hl"><b>Calabrese</b><span class="mk mk--gf">GF</span><span class="mk mk--cf">CF</span><span class="mk mk--sf">SF</span> Pepperoni, onion, fresh tomato, kalamata olives and feta cheese (order jalapenoes for extra spicy).</li>
      <li class="item"><b>Wrenfield Special</b><span class="mk mk--gf">GF</span> Seasoned beef, pepperoni, chunks of fresh cut tomato, with a fresh egg cracked over the top.</li>
      <li class="item"><b>San Marino</b><span class="mk mk--gf">GF</span> Meat Gourmet Pizza Seasoned beef, onion, fresh tomato, tangy paprika sauce and crumbles of feta cheese (order jalapenoes for extra spicy)</li>
      <li class="item"><b>Don Salier</b><span class="mk mk--gf">GF</span> Onion, capsicum, pineapple and a perfect handful of pepperoni.</li>
    </ul>

    <h3 class="sec-head">CHICKEN GOURMET</h3>
    <ul class="items">
      <li class="item item--hl"><b>BBQ Chicken</b><span class="mk mk--gf">GF</span><span class="mk mk--cf">CF</span> Roast chicken fillets, onions and mushrooms with a shake of tangy BBQ sauce.</li>
      <li class="item"><b>Italian Special</b><span class="mk mk--gf">GF</span> Roast chicken fillets, onions, mushrooms, roasted capsicum, sun-dried tomato and a dash of sweet chilli sauce.</li>
      <li class="item"><b>Granada Special</b><span class="mk mk--gf">GF</span> Roast chicken fillets, mushrooms, capsicum, pineapple and smoked bacon.</li>
      <li class="item"><b>Thai Satay</b><span class="mk mk--gf">GF</span> Chargrilled marinated satay chicken, onion, a sprinkle of cracked peanuts and a dab of tangy sour cream sauce.</li>
      <li class="item"><b>Hindu Village</b><span class="mk mk--gf">GF</span> Tandoori chicken, corn, onion and fresh tomato (ask for sour cream for a rich finish).</li>
      <li class="item"><b>Saigon Special</b><span class="mk mk--gf">GF</span> Sesame chicken, mushrooms and onion topped with an aromatic honey and soy sauce.</li>
    </ul>
  </section>

  <section class="vegetarian">
    <h3 class="sec-head">VEGETARIAN GOURMET</h3>
    <ul class="items">
      <li class="item"><b>Mediterranean</b><span class="mk mk--gf">GF</span><span class="mk mk--cf">CF</span> English spinach, feta cheese, onion, fresh cut tomatoes and kalamata olives.</li>
      <li class="item"><b>Super Vegie Special</b><span class="mk mk--gf">GF</span><span class="mk mk--v">V</span> Roasted capsicum, roasted eggplant, artichoke hearts, mushrooms and fresh cut tomato chunks, sprinkled with fresh garlic.</li>
      <li class="item"><b>Pipoli</b><span class="mk mk--gf">GF</span><span class="mk mk--v">V</span><span class="mk mk--sf">SF</span> Mushroom, onion, artichoke hearts, roasted capsicum, olives and a sprinkle of fresh garlic (order jalapenoes to spice it up)</li>
      <li class="item"><b>Alaverdi</b><span class="mk mk--gf">GF</span><span class="mk mk--v">V</span> English spinach, garlic, roasted capsicum, kalamata olives with fresh tomato and a handful of roasted pine nuts.</li>
      <li class="item"><b>La Tomatina</b><span class="mk mk--gf">GF</span> Fresh cut tomato chunks, sun-dried tomatoes, feta cheese and basil, all on a tomato base.</li>
    </ul>
  </section>
</main>

</body>
</html>
```